Detailing informational flyer

I want to design a new flyer for my automotive detailing business. The flyer should use the color scheme from the logo and be easy to read and understand the services we offer.

Industry/Entity Type

Automotive

Font styles to use
Serif
Sans Serif

Colors
3176b5
0255a3
fbed22
33a6d7
0692cd
ffffff

Requirements
Must have
• must include all information from the copy
Nice to have
• include a Glavenor logo such as the image attached

```html
<!DOCTYPE html>
<html lang="en">
<head>
<meta charset="utf-8">
<title>Detail Center &amp; Express Lube Flyers</title>
<link href="https://fonts.googleapis.com/css2?family=Exo+2:wght@700;800&family=Open+Sans:wght@400;600;700;800&display=swap" rel="stylesheet">
<style>
:root{
  --bg:#e6e6e6;
  --navy:#1a2868;
  --navy-deep:#121d52;
  --blue:#0255a3;
  --mid-blue:#3176b5;
  --sky:#33a6d7;
  --cyan:#0692cd;
  --yellow:#fbed22;
  --red:#d7262e;
  --white:#ffffff;
  --grey-text:#c9cfe3;
}
*{box-sizing:border-box;margin:0;padding:0}
html,body{width:1200px;height:873px;overflow:hidden;background:var(--bg)}
body{position:relative;font-family:"Open Sans",Arial,sans-serif}
.flyer{position:absolute;top:52px;width:513px;height:782px;overflow:hidden;
  background:linear-gradient(180deg,var(--navy) 0%,var(--navy-deep) 100%);
  box-shadow:0 6px 14px rgba(0,0,0,.35)}
.flyer--detail{left:56px}
.flyer--lube{left:630px}
.photo{position:absolute;left:0;top:0;width:513px;height:320px}
.photo--car{background:linear-gradient(160deg,#9aa2aa 0%,#3a3f45 45%,#0f1114 100%)}
.photo--oil{background:radial-gradient(circle at 62% 30%,#c98a1c 0%,#6b4a12 18%,#3b3f44 40%,#1a1d21 100%)}
.swoosh{position:absolute;left:0;top:230px;width:513px;height:110px}
.service-line{position:absolute;top:16px;left:0;width:100%;text-align:center;
  font:800 14px/1 "Open Sans",sans-serif;color:var(--white);letter-spacing:.2px;
  text-shadow:0 1px 2px rgba(0,0,0,.6)}
.title{position:absolute;left:-70px;top:322px;width:100%;font-family:"Exo 2",sans-serif;font-weight:800;
  font-size:32px;letter-spacing:1px;text-align:center}
.flyer--detail .title{color:var(--sky)}
.flyer--lube .title{color:var(--red)}
.subtitle{position:absolute;font:800 15px/1 "Open Sans",sans-serif;letter-spacing:3.5px}
.flyer--detail .subtitle{top:368px;left:80px;color:var(--yellow)}
.flyer--lube .subtitle{top:374px;left:64px;color:var(--grey-text);font-size:13px}
.services{position:absolute;top:404px;left:22px;width:472px;display:flex;flex-direction:column;gap:11px}
.service{display:flex;gap:12px;align-items:flex-start}
.service__icon{flex:0 0 42px;height:42px;border-radius:50%;background:var(--blue);
  border:2px solid var(--mid-blue)}
.service__icon svg{width:38px;height:38px}
.service p{font-size:9.6px;line-height:1.2;color:var(--white);text-align:justify}
.service strong{color:var(--yellow);font-weight:800}
.closing{position:absolute;top:690px;left:22px;width:470px;display:flex;align-items:center;justify-content:space-between}
.cta-note{font:700 10px/1 "Open Sans",sans-serif;color:var(--yellow)}
.partner{display:flex;align-items:center;gap:4px;
  font:800 12px/1 "Open Sans",sans-serif;color:var(--yellow)}
.partner .dot{width:9px;height:9px;border-radius:50%;background:var(--yellow)}
.phone{position:absolute;top:722px;left:148px;width:216px;height:32px;border-radius:16px;
  background:linear-gradient(180deg,#2fa6e3,var(--blue));display:flex;align-items:center;
  justify-content:center;gap:8px;font:700 18px/1 "Open Sans",sans-serif;color:var(--white);
  box-shadow:0 2px 4px rgba(0,0,0,.4);z-index:2}
.address-bar{position:absolute;left:0;bottom:0;width:100%;height:38px;display:flex;
  align-items:center;justify-content:center;padding-top:6px;font:800 13.5px/1 "Open Sans",sans-serif;letter-spacing:.6px}
.flyer--detail .address-bar{background:var(--yellow);color:var(--navy-deep)}
.flyer--lube .address-bar{background:var(--red);color:var(--white)}
.section-head{position:absolute;top:412px;left:21px;font:800 14px/1 "Open Sans",sans-serif;color:var(--sky)}
.checklist{position:absolute;top:442px;list-style:none}
.checklist--a{left:20px}
.checklist--b{left:245px}
.checklist li{height:27px;display:flex;align-items:center;gap:6px;font:600 10.4px/1 "Open Sans",sans-serif;color:var(--white)}
.checklist li small{font-size:6px}
.checklist svg{width:13px;height:13px;flex:0 0 13px}
.offer{position:absolute;top:637px;left:22px;width:472px;height:72px;border:1.5px solid #7f8bb8;
  border-radius:8px;display:flex;align-items:center;justify-content:center;text-align:center;
  font:700 20px/1.25 "Open Sans",sans-serif;color:var(--sky);letter-spacing:.5px}
</style>
</head>
<body>

<section class="flyer flyer--detail">
  <div class="photo photo--car" role="img" aria-label="Photo of a glossy black sedan inside a car wash"></div>
  <svg class="swoosh" viewBox="0 0 513 110" preserveAspectRatio="none" aria-hidden="true">
    <path d="M0 60 Q220 20 513 0 L513 30 Q240 50 0 100Z" fill="#fbed22"/>
    <path d="M0 88 Q240 45 513 26 L513 110 L0 110Z" fill="#1a2868"/>
  </svg>
  <div class="service-line">CAR WASH · OIL LUBE &amp; FILTER SERVICE · AUTO DETAILING SERVICE</div>
  <h1 class="title">DETAIL CENTER</h1>
  <div class="subtitle">BROOKVIEW CARWASH</div>

  <div class="services">
    <div class="service">
      <div class="service__icon"><svg viewBox="0 0 38 38"><path d="M9 23 L12 16 H26 L29 23 V27 H9Z" fill="#fff"/><circle cx="13" cy="27" r="2.5" fill="#0255a3"/><circle cx="25" cy="27" r="2.5" fill="#0255a3"/></svg></div>
      <p><strong>EXTERIOR DETAILING INCLUDES:</strong> We wash, clay, compound, polish, and wax, as needed to restore the deep rich gloss and provide a durable shine for that "new car" look. This process removes light oxidation from the vehicle and protects the clear coat finish. Finishing touches include rim cleaning and tire shine.</p>
    </div>
    <div class="service">
      <div class="service__icon"><svg viewBox="0 0 38 38"><path d="M14 10 L18 10 L20 22 L27 22 L27 27 L15 27Z" fill="#fff"/></svg></div>
      <p><strong>INTERIOR DETAILING SHAMPOO INCLUDES:</strong> We perform a deep cleaning of the interior such as the dashboard, door jams, center console, trunk area, upholstered seats, and all carpets and mats. This process will remove soils and most stains. Windows are cleaned inside and out. All leather is dressed to provide a protective finish. Air freshener is available upon request.</p>
    </div>
    <div class="service">
      <div class="service__icon"><svg viewBox="0 0 38 38"><circle cx="19" cy="19" r="9" fill="#fbed22"/><circle cx="19" cy="19" r="3.5" fill="#0255a3"/></svg></div>
      <p><strong>MINI DETAIL/ VIP SERVICE INCLUDES:</strong> Brookview Special Wash with triple polish wax, Glavenor Shield protectant, tire shine, and a detailed and gentle cleaning of the upholstery. 4 rubber or carpet mats are shampooed. All interior surfaces are dressed including dashboard, door panels, center console. This is followed by a detailed carpet and upholstery vacuum with compressed air to remove dirt from hard to reach places. For added shine ask about adding on our express wax service to your mini detail package.</p>
    </div>
    <div class="service">
      <div class="service__icon"><svg viewBox="0 0 38 38"><path d="M12 13 Q20 13 20 19 Q20 25 12 25Z" fill="#fbed22"/><path d="M23 14 H29 M23 19 H30 M23 24 H29" stroke="#fbed22" stroke-width="2"/></svg></div>
      <p><strong>HEADLIGHT RESTORATION:</strong> This shop proudly offers the Headlight Service, which can polish or restore your headlight to a clear, safe condition at a fraction of the cost of headlight replacement! Restore the lens to a clear, shiny &amp; safe condition.</p>
    </div>
  </div>

  <div class="closing">
    <div class="cta-note">Ask to speak to a manager about scheduling any of our detailing services.</div>
    <div class="partner"><span class="dot"></span>GLAVENOR</div>
  </div>

  <div class="phone">
    <svg width="18" height="18" viewBox="0 0 18 18" aria-hidden="true"><circle cx="9" cy="9" r="8" fill="none" stroke="#fff" stroke-width="1.5"/><path d="M6 5 L7.5 5 L8.2 7 L7.2 7.8 Q8 9.8 10.2 10.8 L11 9.8 L13 10.5 L13 12 Q9 13 6 8Z" fill="#fff"/></svg>
    +1 555-010-4400
  </div>
  <div class="address-bar">48-20 Harbor Ave Elm Gardens 11400</div>
</section>

<section class="flyer flyer--lube">
  <div class="photo photo--oil" role="img" aria-label="Photo of motor oil being poured into an engine"></div>
  <svg class="swoosh" viewBox="0 0 513 110" preserveAspectRatio="none" aria-hidden="true">
    <path d="M0 60 Q220 20 513 0 L513 30 Q240 50 0 100Z" fill="#d7262e"/>
    <path d="M0 88 Q240 45 513 26 L513 110 L0 110Z" fill="#1a2868"/>
  </svg>
  <div class="service-line">CAR WASH · OIL LUBE &amp; FILTER SERVICE · AUTO DETAILING SERVICE</div>
  <h1 class="title">EXPRESS LUBE</h1>
  <div class="subtitle">BROOKVIEW CARWASH</div>

  <div class="section-head">OIL CHANGE</div>
  <ul class="checklist checklist--a">
    <li><svg viewBox="0 0 13 13"><circle cx="6.5" cy="6.5" r="5.5" fill="none" stroke="#33a6d7"/><path d="M4 6.7 L6 8.5 L9.2 4.6" fill="none" stroke="#33a6d7" stroke-width="1.3"/></svg>UP TO 5 QTS. OF VELTRIX BULK OIL</li>
    <li><svg viewBox="0 0 13 13"><circle cx="6.5" cy="6.5" r="5.5" fill="none" stroke="#33a6d7"/><path d="M4 6.7 L6 8.5 L9.2 4.6" fill="none" stroke="#33a6d7" stroke-width="1.3"/></svg>QUALITY OIL FILTER</li>
    <li><svg viewBox="0 0 13 13"><circle cx="6.5" cy="6.5" r="5.5" fill="none" stroke="#33a6d7"/><path d="M4 6.7 L6 8.5 L9.2 4.6" fill="none" stroke="#33a6d7" stroke-width="1.3"/></svg>COMPLETE CHASSIS LUBRICATION</li>
    <li><svg viewBox="0 0 13 13"><circle cx="6.5" cy="6.5" r="5.5" fill="none" stroke="#33a6d7"/><path d="M4 6.7 L6 8.5 L9.2 4.6" fill="none" stroke="#33a6d7" stroke-width="1.3"/></svg>CHECK &amp; FILL BRAKE FLUID</li>
    <li><svg viewBox="0 0 13 13"><circle cx="6.5" cy="6.5" r="5.5" fill="none" stroke="#33a6d7"/><path d="M4 6.7 L6 8.5 L9.2 4.6" fill="none" stroke="#33a6d7" stroke-width="1.3"/></svg>CHECK &amp; TRANSMISSION FLUID</li>
    <li><svg viewBox="0 0 13 13"><circle cx="6.5" cy="6.5" r="5.5" fill="none" stroke="#33a6d7"/><path d="M4 6.7 L6 8.5 L9.2 4.6" fill="none" stroke="#33a6d7" stroke-width="1.3"/></svg>CHECK &amp; FILL DIFFERENT FLUID</li>
    <li><svg viewBox="0 0 13 13"><circle cx="6.5" cy="6.5" r="5.5" fill="none" stroke="#33a6d7"/><path d="M4 6.7 L6 8.5 L9.2 4.6" fill="none" stroke="#33a6d7" stroke-width="1.3"/></svg>CHECK &amp; FILL POWER STEERING FLUID</li>
  </ul>
  <ul class="checklist checklist--b">
    <li><svg viewBox="0 0 13 13"><circle cx="6.5" cy="6.5" r="5.5" fill="none" stroke="#33a6d7"/><path d="M4 6.7 L6 8.5 L9.2 4.6" fill="none" stroke="#33a6d7" stroke-width="1.3"/></svg>CHECK &amp; FILL WASHER FLUID</li>
    <li><svg viewBox="0 0 13 13"><circle cx="6.5" cy="6.5" r="5.5" fill="none" stroke="#33a6d7"/><path d="M4 6.7 L6 8.5 L9.2 4.6" fill="none" stroke="#33a6d7" stroke-width="1.3"/></svg>CHECK &amp; FILL ANTIFREEZE</li>
    <li><svg viewBox="0 0 13 13"><circle cx="6.5" cy="6.5" r="5.5" fill="none" stroke="#33a6d7"/><path d="M4 6.7 L6 8.5 L9.2 4.6" fill="none" stroke="#33a6d7" stroke-width="1.3"/></svg>CHECK BREATHER &amp; AIR FILTER <small>(CHARGE IF REPLACED)</small></li>
    <li><svg viewBox="0 0 13 13"><circle cx="6.5" cy="6.5" r="5.5" fill="none" stroke="#33a6d7"/><path d="M4 6.7 L6 8.5 L9.2 4.6" fill="none" stroke="#33a6d7" stroke-width="1.3"/></svg>CHECK WIPER BLADES <small>(CHARGE IF REPLACED)</small></li>
    <li><svg viewBox="0 0 13 13"><circle cx="6.5" cy="6.5" r="5.5" fill="none" stroke="#33a6d7"/><path d="M4 6.7 L6 8.5 L9.2 4.6" fill="none" stroke="#33a6d7" stroke-width="1.3"/></svg>CHECK TIRE PRESSURE &amp; INFLATE</li>
    <li><svg viewBox="0 0 13 13"><circle cx="6.5" cy="6.5" r="5.5" fill="none" stroke="#33a6d7"/><path d="M4 6.7 L6 8.5 L9.2 4.6" fill="none" stroke="#33a6d7" stroke-width="1.3"/></svg>LUBRICATE DOOR HINGES</li>
    <li><svg viewBox="0 0 13 13"><circle cx="6.5" cy="6.5" r="5.5" fill="none" stroke="#33a6d7"/><path d="M4 6.7 L6 8.5 L9.2 4.6" fill="none" stroke="#33a6d7" stroke-width="1.3"/></svg>COMPUTERIZED SERVICE RECORD</li>
  </ul>

  <div class="offer">EVERY OIL CHANGE INCLUDES A<br>FREE CAR WASH</div>

  <div class="phone">
    <svg width="18" height="18" viewBox="0 0 18 18" aria-hidden="true"><circle cx="9" cy="9" r="8" fill="none" stroke="#fff" stroke-width="1.5"/><path d="M6 5 L7.5 5 L8.2 7 L7.2 7.8 Q8 9.8 10.2 10.8 L11 9.8 L13 10.5 L13 12 Q9 13 6 8Z" fill="#fff"/></svg>
    +1 555-010-4400
  </div>
  <div class="address-bar">48-20 Harbor Ave Elm Gardens 11400</div>
</section>

</body>
</html>
```